I need a direct mail postcard made up for my marketing campaign

I am starting a marketing campaign and need a design for a post card. I own an iron door company and need to have before and after images on the post card to showcase what our work looks like. I have provided pictures to use below.

The design needs to be two sided. The logo should be on the front.

The tag line for this campaign is: Design the smile your home deserves.

Words to also use: Distinctive style, Work of Art, One-of-a-Kind, Elegant, Modern, Innovative, Unique

My information for the card
Name: Dean Harlowe
Phone number: (555)-318-2764
Email: Dean@wroughtgatestudio.example

The US postal system is very picky as to what can be sent in the mail. The only requirement they have is for the address. There needs to be a 2inch (50.8mm) by 4inch (101.6mm) blank space on the bottom right hand corner on the back of the card.

Target Market(s)

Home owners

Industry/Entity Type

Home Improvement

Font styles to use
Serif
Decorative

Colors
0555a3
ffffff
ec1f27

Requirements
Must have
• My logo, My contact information, before and after pictures
• Provided 3D images
Nice to have
• Words that describe iron doors
• A contrast between contemporary and ornate doors.

```html
<!DOCTYPE html>
<html lang="en">
<head>
<meta charset="utf-8">
<title>Wrought Gate Studio – Direct Mail Postcard</title>
<link href="https://fonts.googleapis.com/css2?family=Dosis:wght@500;600;700&family=Playfair+Display:ital,wght@0,900;1,400&display=swap" rel="stylesheet">
<style>
  :root{
    --brand-blue:#0555a3;
    --deep-blue:#0a3f82;
    --light-blue:#3d7cc9;
    --accent-red:#ec1f27;
    --white:#ffffff;
    --ink-blue:#0b3f86;
    --slate:#45607c;
    --page:#e8eaee;
    --door-brown:#5a2e1c;
  }
  *{box-sizing:border-box;margin:0;padding:0}
  html,body{width:1200px;height:800px;overflow:hidden}
  body{background:var(--page);font-family:"Dosis",sans-serif;position:relative}

  .postcard{position:absolute;top:212px;width:555px;height:375px;background:var(--white);overflow:hidden;box-shadow:0 6px 18px rgba(0,0,0,.18)}
  .postcard--front{left:30px}
  .postcard--back{left:615px}

  /* front */
  .front__hero{position:absolute;left:0;top:0;width:100%;height:237px;background:linear-gradient(180deg,#1f68b8 0%,var(--brand-blue) 55%,#074c95 100%)}
  .front__headline{position:absolute;left:22px;top:24px;font-family:"Playfair Display",serif;font-weight:900;font-size:46px;color:var(--white);letter-spacing:-1px;line-height:1;white-space:nowrap;transform:scaleX(.78);transform-origin:left top}
  .front__tagline{position:absolute;left:0;width:330px;top:76px;text-align:right;font-family:"Playfair Display",serif;font-style:italic;font-size:21px;color:var(--white)}
  .front__rule{position:absolute;left:30px;width:305px;height:1px;background:rgba(255,255,255,.75)}
  .front__rule--top{top:125px}
  .front__rule--bottom{top:213px}
  .feature-words{position:absolute;left:18px;width:320px;top:133px;text-align:center;color:var(--white);font-weight:600;font-size:18px;line-height:25px}
  .feature-words span{white-space:nowrap}
  .feature-words span::before{content:"";display:inline-block;width:0;height:0;border-top:5px solid transparent;border-bottom:5px solid transparent;border-left:6px solid var(--deep-blue);margin:0 3px 1px 4px;vertical-align:middle}

  .showcase{position:absolute;border-radius:10px;overflow:hidden;display:flex;background:var(--white)}
  .front__showcase{left:350px;top:28px;width:185px;height:195px;padding:3px}
  .showcase__photo{flex:1;position:relative}
  .showcase__photo--before-wood{background:linear-gradient(135deg,#7a3b22,#4e2414)}
  .showcase__photo--after-iron{background:linear-gradient(180deg,#3a3a3c 0%,#6b5427 45%,#2a2a2c 100%);margin-left:3px}
  .showcase__photo--before-white{background:linear-gradient(180deg,#e8e1d6,#f6f3ee)}
  .showcase__photo--after-dark{background:linear-gradient(180deg,#3b3d57,#1e1f33);margin-left:2px}
  .showcase__label{position:absolute;bottom:0;background:var(--accent-red);color:var(--white);font-weight:700}
  .front__showcase .showcase__label{font-size:13px;padding:2px 10px}
  .showcase__label--before{left:0;border-top-right-radius:6px}
  .showcase__label--after{right:0;border-top-left-radius:6px}

  .front__portrait{position:absolute;left:22px;top:222px;width:120px;height:128px;border:3px solid var(--slate);border-radius:6px;background:linear-gradient(180deg,#b9c0c8 0%,#8f99a4 60%,#2c3140 100%)}
  .contact{position:absolute;left:158px;top:248px;color:var(--ink-blue)}
  .contact__name{font-weight:700;font-size:30px;line-height:1.1}
  .contact__phone{font-weight:600;font-size:23px;line-height:1.2}
  .contact__email{font-weight:600;font-size:13.5px;margin-top:4px}
  .front__door-art{position:absolute;top:248px;height:102px;border:3px solid var(--slate);background:var(--door-brown)}
  .front__door-art--arched{left:390px;width:78px}
  .front__door-art--modern{left:474px;width:62px}
  .front__footer-band{position:absolute;left:0;bottom:0;width:100%;height:18px;background:var(--slate)}

  /* back */
  .back__header{position:absolute;left:0;top:0;width:100%;height:88px;background:linear-gradient(90deg,var(--brand-blue),var(--light-blue))}
  .back__phone{position:absolute;left:28px;top:20px;color:var(--white);font-weight:700;font-size:40px}
  .back__stamp-box{position:absolute;right:24px;top:16px;width:62px;height:72px;background:var(--white);border:1.5px solid #6d7077}
  .benefit-list{position:absolute;left:30px;top:110px;list-style:none;color:var(--brand-blue);font-weight:600;font-size:22px;line-height:34px}
  .benefit-list li::before{content:"";display:inline-block;width:10px;height:10px;border-radius:50%;background:var(--brand-blue);margin-right:9px;vertical-align:middle}
  .brand-mark{position:absolute;left:235px;top:112px;display:flex;align-items:center;gap:6px;color:var(--brand-blue);font-weight:700;font-size:15px;line-height:1.05}
  .brand-mark__dot{width:14px;height:14px;border-radius:50%;background:var(--brand-blue)}
  .back__showcase{left:222px;top:190px;width:128px;height:142px;padding:2px;border:2px solid var(--brand-blue)}
  .back__showcase .showcase__label{font-size:10px;padding:1px 6px}
  .back__footer-band{position:absolute;left:0;bottom:0;width:100%;height:16px;background:#6f93c6}
</style>
</head>
<body>

<section class="postcard postcard--front" aria-label="Postcard front">
  <div class="front__hero"></div>
  <h1 class="front__headline">Design the Smile</h1>
  <p class="front__tagline">your home deserves.</p>
  <div class="front__rule front__rule--top"></div>
  <p class="feature-words">
    <span>Distinctive style</span> <span>Work of Art</span><br>
    <span>One-of-a-Kind</span> <span>Elegant</span> <span>Modern</span><br>
    <span>Innovative</span> <span>Unique</span>
  </p>
  <div class="front__rule front__rule--bottom"></div>

  <div class="showcase front__showcase">
    <div class="showcase__photo showcase__photo--before-wood" role="img" aria-label="Before photo: worn wooden double front door">
      <span class="showcase__label showcase__label--before">Before</span>
    </div>
    <div class="showcase__photo showcase__photo--after-iron" role="img" aria-label="After photo: ornate wrought iron double door with glass">
      <span class="showcase__label showcase__label--after">After</span>
    </div>
  </div>

  <div class="front__portrait" role="img" aria-label="Portrait photo of Dean Harlowe"></div>
  <div class="contact">
    <p class="contact__name">Dean Harlowe</p>
    <p class="contact__phone">Ph: (555)-318-2764</p>
    <p class="contact__email">E: Dean@wroughtgatestudio.example</p>
  </div>
  <div class="front__door-art front__door-art--arched" role="img" aria-label="3D rendering of an arched contemporary iron door"></div>
  <div class="front__door-art front__door-art--modern" role="img" aria-label="3D rendering of a modern iron door with sidelight"></div>
  <div class="front__footer-band"></div>
</section>

<section class="postcard postcard--back" aria-label="Postcard back">
  <div class="back__header"></div>
  <p class="back__phone">Ph: (555)-318-2764</p>
  <div class="back__stamp-box"></div>
  <ul class="benefit-list">
    <li>Distinctive style</li>
    <li>Work of Art</li>
    <li>One-of-a-Kind</li>
  </ul>
  <div class="brand-mark">
    <span class="brand-mark__dot"></span>
    <span>Wrought Gate<br>Studio</span>
  </div>
  <div class="showcase back__showcase">
    <div class="showcase__photo showcase__photo--before-white" role="img" aria-label="Before photo: plain white front door">
      <span class="showcase__label showcase__label--before">Before</span>
    </div>
    <div class="showcase__photo showcase__photo--after-dark" role="img" aria-label="After photo: arched iron double door with wreaths">
      <span class="showcase__label showcase__label--after">After</span>
    </div>
  </div>
  <div class="back__footer-band"></div>
</section>

</body>
</html>
```